Law Firm Website

We are looking to update our old, tired and very flat website. We have someone who will code and host the site but we need some design inspiration. The website will consist of no more than 2/3 pages, possibly with pop-ups for information. We already have all the blurb. We would like something distinctive, clean and eye-catching, using the purple and white theme that we already use on our firm stationery. Examples uploaded. Current website URL is www.dunmorewillett.example.

Industry/Entity Type

Law Firm

```html
<!DOCTYPE html>
<html lang="en">
<head>
<meta charset="utf-8">
<title>Dunmore &amp; Willett Solicitors</title>
<link rel="stylesheet" href="https://fonts.googleapis.com/css2?family=Bebas+Neue&family=Libre+Baskerville&family=Roboto:wght@300;400&family=Caveat:wght@500&display=swap">
<style>
  :root {
    --purple: #5b4585;
    --purple-text: #4e3f82;
    --band-grey: #dcdbe0;
    --panel-grey: #e7e6eb;
    --nav-ink: #3b3b3b;
    --body-ink: #4a4a4a;
    --white: #ffffff;
    --footer-ink: #9a9a9a;
  }
  * { margin: 0; padding: 0; box-sizing: border-box; }
  html, body { width: 857px; height: 1200px; overflow: hidden; background: var(--white); }
  body { position: relative; font-family: "Roboto", Arial, sans-serif; font-weight: 300; color: var(--body-ink); }

  .masthead { position: absolute; left: 0; top: 0; width: 857px; height: 200px; background: var(--band-grey); }
  .masthead-top { position: absolute; left: 0; top: 0; width: 857px; height: 97px; background: var(--white); }
  .firm-name {
    position: absolute; left: 0; top: 54px; width: 857px; text-align: center;
    font-family: "Libre Baskerville", Georgia, serif; font-size: 36px; color: var(--purple-text);
  }
  .nav-rule { position: absolute; left: 150px; top: 137px; width: 557px; height: 1px; background: var(--purple); }
  .main-nav {
    position: absolute; left: 0; top: 150px; width: 857px;
    display: flex; justify-content: center; gap: 28px;
    font-family: "Bebas Neue", Impact, sans-serif; font-size: 24px; color: var(--nav-ink); letter-spacing: 0.3px;
  }

  .hero {
    position: absolute; left: 0; top: 200px; width: 857px; height: 417px;
    background: linear-gradient(110deg, #2a2e38 0%, #5a5e66 35%, #8a8e96 55%, #3a4152 75%, #1e2434 100%);
    overflow: hidden;
  }
  .hero-sheen { position: absolute; left: 0; top: 57px; width: 857px; height: 146px; background: rgba(255,255,255,0.08); }
  .hero-slate { position: absolute; left: 0; top: 345px; width: 324px; height: 72px; background: rgba(255,255,255,0.12); }
  .hero-title, .hero-tagline {
    position: absolute; left: 26px; color: var(--white); font-family: "Roboto", sans-serif; font-weight: 300;
    line-height: 47px; font-size: 45px;
  }
  .hero-title { top: 76px; }
  .hero-tagline { top: 300px; }

  .about { position: absolute; left: 0; top: 617px; width: 857px; height: 236px; background: var(--panel-grey); }
  .about-frame { position: absolute; left: 9px; top: 10px; width: 248px; height: 226px; background: #f2f2f4; }
  .about-photo {
    position: absolute; left: 26px; top: 10px; width: 214px; height: 226px;
    background: linear-gradient(180deg, #4a7bc6 0%, #9bb7df 30%, #bfb39a 55%, #7d7566 100%);
  }
  .about-text { position: absolute; left: 285px; top: 26px; width: 560px; font-size: 15px; line-height: 19px; }
  .about-text p { margin-bottom: 18px; }
  .about-text .single-line { white-space: nowrap; }
  .about-text .name { font-weight: 400; color: #333; }

  .expertise { position: absolute; left: 0; top: 853px; width: 857px; height: 171px; background: var(--panel-grey); }
  .expertise-label {
    position: absolute; left: 8px; top: 0; width: 248px; height: 171px; background: var(--purple);
    color: var(--white); text-align: right; padding-right: 20px; padding-top: 52px;
  }
  .expertise-label .small { display: block; font-size: 21px; line-height: 24px; }
  .expertise-label .large { display: block; font-size: 40px; line-height: 42px; }
  .practice-list { position: absolute; top: 8px; list-style: none; font-size: 15px; line-height: 20px; }
  .practice-list.left { left: 286px; }
  .practice-list.right { left: 569px; }

  .testimonials { position: absolute; left: 0; top: 1024px; width: 857px; height: 109px; background: var(--panel-grey); }
  .testimonials h2 {
    position: absolute; left: 0; top: 33px; width: 832px; text-align: center;
    font-weight: 300; font-size: 16px; color: #333;
  }
  .quote {
    position: absolute; left: 44px; top: 53px; width: 769px; text-align: center; white-space: nowrap;
    font-family: "Caveat", cursive; font-weight: 500; font-size: 23px; color: #333;
  }
  .quote-mark { position: absolute; font-family: Georgia, serif; font-size: 38px; font-weight: 700; color: #555; }

  .site-footer { position: absolute; left: 0; top: 1133px; width: 857px; height: 67px; background: var(--white); }
  .partner-badge { position: absolute; left: 9px; top: 9px; width: 147px; height: 45px; background: #f3f3f3; border: 1px solid #e4e4e4; }
  .partner-badge .dot { position: absolute; left: 8px; top: 13px; width: 18px; height: 18px; background: #d8242d; }
  .copyright { position: absolute; left: 0; top: 10px; width: 857px; text-align: center; font-size: 12px; color: var(--footer-ink); }
  .legal-links { position: absolute; right: 4px; top: 10px; font-size: 12px; color: var(--footer-ink); }
</style>
</head>
<body>
  <header class="masthead">
    <div class="masthead-top"></div>
    <div class="firm-name">Dunmore &amp; Willett</div>
    <div class="nav-rule"></div>
    <nav class="main-nav">
      <span>Home</span>
      <span>Area of Expertise</span>
      <span>Edward Dunmore</span>
      <span>Martin Willett</span>
      <span>Contact</span>
    </nav>
  </header>

  <section class="hero" role="img" aria-label="Photograph of solicitors and clients reviewing documents at a meeting table">
    <div class="hero-sheen"></div>
    <div class="hero-slate"></div>
    <h1 class="hero-title">Dunmore &amp; Willett<br>Solicitors</h1>
    <p class="hero-tagline">for the service<br>you deserve</p>
  </section>

  <section class="about">
    <div class="about-frame"></div>
    <div class="about-photo" role="img" aria-label="Photograph of a Gothic court building against a blue sky"></div>
    <div class="about-text">
      <p>DUNMORE and WILLETT is a firm of solicitors with offices in Thornbury, London and Ashcombe, Hertfordshire. This firm is authorised and regulated by the Legal Practice Standards Board, no.608213.</p>
      <p>VAT registered number: 481 2097 36</p>
      <p class="single-line">Professional rules can be viewed on www.practiceboard.example/code-of-conduct.</p>
      <p>Know More about <span class="name">Edward Dunmore</span> &amp; <span class="name">Martin Willett</span></p>
    </div>
  </section>

  <section class="expertise">
    <div class="expertise-label">
      <span class="small">Areas of</span>
      <span class="large">Expertise</span>
    </div>
    <ul class="practice-list left">
      <li>Company Matters</li>
      <li>Commercial Matters</li>
      <li>Commercial Crime</li>
      <li>Litigation / Disputes</li>
      <li>Insolvency</li>
      <li>Residential Conveyancing</li>
      <li>Commercial Conveyancing</li>
      <li>Wills &amp; Probate</li>
    </ul>
    <ul class="practice-list right">
      <li>Estate Planning</li>
      <li>Powers of Attorney</li>
      <li>Care of the Elderly</li>
      <li>Court of Protection</li>
      <li>Divorce / Family</li>
      <li>Pre-Nuptial Agreements</li>
      <li>Intellectual Property</li>
      <li>Media Law</li>
    </ul>
  </section>

  <section class="testimonials">
    <h2>CLIENT TESTIMONIALS</h2>
    <span class="quote-mark" style="left:36px; top:36px;">&lsquo;</span>
    <p class="quote">thank you, thank you, thank you. your hard work and dedication has changed my life for better</p>
    <span class="quote-mark" style="left:811px; top:30px;">&rsquo;</span>
  </section>

  <footer class="site-footer">
    <div class="partner-badge"><span class="dot"></span></div>
    <div class="copyright">&copy; 2014. Dunmore &amp; Willett</div>
    <div class="legal-links">Legal Notice &nbsp;|&nbsp; Privacy Policy</div>
  </footer>
</body>
</html>
```